A 'new law' boutique Australian law firm that provides specialist employment law and people managem

We value helping clients create results with respect workplaces. What differentiates us is we provide actionable training in understanding and dealing with people and ensure legal compliance fits with this approach. We would like a fresh approach to our training overview documents that we currently use in our current law firm (6 attached). Please use pictures, symbols etc consistent with our non-traditional law approach that captures the approach of each training session.. Attached is the logo and draft letterhead for Brindle Legal which will launch soon.

Target Market(s)

HR Managers and in-house lawyers (non employment specialists) in mid-large Australian companies that are progressive with a relationship based approach to managing employee behaviours and disputes.

Industry/Entity Type

Human Resource

Font styles to use
Sans Serif

Colors
3176b5
33a6d7

Requirements
Must have
• 1 or 2 page PDF for each of the 6 documents that the wording supplied goes into your design which will be pretty similar as we want consistency with our documents

```html
<!DOCTYPE html>
<html lang="en">
<head>
<meta charset="utf-8">
<title>Contact Officer Training – Brindle Legal</title>
<link href="https://fonts.googleapis.com/css2?family=Montserrat:wght@800;900&family=Open+Sans:wght@400;600;700&display=swap" rel="stylesheet">
<style>
  :root {
    --brand-blue: #3176b5;
    --brand-sky: #33a6d7;
    --title-blue: #1d6cbc;
    --band-blue: #2a78c4;
    --ink: #3a3a3c;
    --grey-label: #d7d8da;
    --grey-desc: #bdbec1;
    --grey-heading: #7b7c7f;
    --stage: #1b1c1f;
    --paper: #ffffff;
  }
  * { box-sizing: border-box; margin: 0; padding: 0; }
  html, body { width: 1200px; height: 848px; overflow: hidden; }
  body { background: var(--stage); font-family: "Open Sans", Arial, sans-serif; color: var(--ink); }

  .flyer {
    position: absolute; left: 317px; top: 24px;
    width: 566px; height: 800px;
    background: var(--paper); overflow: hidden;
  }
  .flyer-shapes { position: absolute; inset: 0; }

  .title {
    position: absolute; left: 170px; top: 26px;
    font-family: "Montserrat", Arial, sans-serif; font-weight: 900;
    color: var(--title-blue); line-height: .9; text-transform: uppercase;
  }
  .title-top { display: block; font-size: 24px; letter-spacing: .5px; }
  .title-main { display: block; font-size: 54px; letter-spacing: 1px; }

  .need { position: absolute; left: 24px; top: 176px; width: 262px; color: #fff; }
  .need h2, .overview h2, .outcomes h2 {
    font-family: "Montserrat", Arial, sans-serif; font-weight: 800; text-transform: uppercase;
  }
  .need h2 { font-size: 15px; margin-bottom: 8px; }
  .need p, .challenge p { font-size: 8px; line-height: 1.4; margin-bottom: 7px; }
  .challenge { position: absolute; left: 300px; top: 268px; width: 245px; color: #fff; }

  .overview { position: absolute; left: 24px; top: 330px; width: 518px; }
  .overview h2 { font-size: 16px; color: var(--grey-heading); margin-bottom: 6px; }
  .overview-table { width: 100%; border-collapse: collapse; font-size: 6.6px; line-height: 1.35; }
  .overview-table td { padding: 5px 7px; border-bottom: 1px solid #fff; vertical-align: middle; }
  .topic { width: 128px; background: var(--grey-label); font-weight: 600; }
  .detail { background: var(--grey-desc); border-left: 1px solid #fff; }

  .outcomes { position: absolute; left: 24px; top: 612px; width: 400px; }
  .outcomes h2 { font-size: 16px; color: var(--title-blue); margin-bottom: 4px; }
  .outcomes-intro { font-size: 7.8px; font-weight: 700; margin-bottom: 3px; }
  .outcomes ol { list-style: none; font-size: 7.8px; line-height: 1.4; }

  .brand {
    position: absolute; right: 26px; top: 688px;
    display: flex; align-items: center; gap: 6px;
    font-weight: 700; font-size: 22px; color: var(--brand-blue); text-transform: uppercase; letter-spacing: .5px;
  }
  .brand-dot { width: 14px; height: 14px; border-radius: 50%; background: var(--brand-sky); }
  .contact {
    position: absolute; right: 26px; top: 740px; text-align: right;
    color: #fff; font-size: 7.8px; font-weight: 700; line-height: 1.45;
  }
</style>
</head>
<body>
<article class="flyer">
  <svg class="flyer-shapes" width="566" height="800" viewBox="0 0 566 800">
    <defs>
      <linearGradient id="heroTone" x1="0" y1="0" x2="1" y2="1">
        <stop offset="0" stop-color="#f4f6f9"/>
        <stop offset=".55" stop-color="#dfe6ee"/>
        <stop offset="1" stop-color="#8fa9c9"/>
      </linearGradient>
    </defs>
    <polygon points="170,0 566,0 566,300 250,160" fill="url(#heroTone)" role="img" aria-label="Photo of a meeting with hands taking notes on paper"/>
    <polygon points="0,165 250,150 566,300 566,430 0,305" fill="var(--band-blue)"/>
    <polygon points="0,800 566,800 566,738 40,775" fill="var(--band-blue)"/>
  </svg>

  <h1 class="title"><span class="title-top">Contact Officer</span><span class="title-main">Training</span></h1>

  <section class="need">
    <h2>Training Need</h2>
    <p>Unlawful or inappropriate behavior in the workplace that is left unaddressed can impact on productivity and employee retention. Claims can be costly in terms of time and money as well as the impact on mental health from being involved in uncomfortable adversarial processes.</p>
    <p>Clear policies and procedures explaining the organisation's workplace behavior expectations and how grievances will be managed are a minimum compliance requirement.</p>
  </section>

  <section class="challenge">
    <p>The challenge is ensuring that employees understand the directions contained in those policies, what is unlawful and inappropriate behaviour and the options available to address those behaviours if they experience them or engage in them.</p>
    <p>Well trained Contact Officers provide another resource to assist the organisation to provide a safe and respectful workplace.</p>
  </section>

  <section class="overview">
    <h2>Overview</h2>
    <table class="overview-table">
      <tr><td class="topic">Discrimination</td><td class="detail">What is direct and indirect discrimination? What are the prescribed attributes? What are the exceptions to the general rules? Practical examples of behaviour that may be discriminatory.</td></tr>
      <tr><td class="topic">Harassment</td><td class="detail">What is harassment? Are protected attributes relevant to harassment? What is the difference between harassment and sexual harassment? How does the reasonable person test work in relation to harassment? Practical examples of behaviour that may be harassment or sexual harassment.</td></tr>
      <tr><td class="topic">Bullying</td><td class="detail">What is bullying. Explain how bullying differs to discrimination or inappropriate behaviour. Performance management – what will and will not be bullying? Is all workplace conflict bullying? Practical examples of behaviour that may be bullying.</td></tr>
      <tr><td class="topic">Victimisation and Vilification</td><td class="detail">What is victimisation? What is Vilification?</td></tr>
      <tr><td class="topic">Adverse Action</td><td class="detail">What is adverse action and how does it differ to other unlawful behaviour? What is a workplace right? When is it unlawful to terminate employment because of an employee's absence? How are the protected attributes relevant to adverse action?</td></tr>
      <tr><td class="topic">The Contact Officer's role</td><td class="detail">How to perform your role when approached by an employee – the 6 step approach. What not to do. What are the obligations with regard to confidentiality?</td></tr>
      <tr><td class="topic">Grievance Options</td><td class="detail">Explore the options of complaint management – self management, internal informal management, formal internal management. How do they compare and what are the advantages and disadvantages of each approach. Is doing nothing an option? External options – advantages and disadvantages. Who decides which option?</td></tr>
      <tr><td class="topic">Test Learning</td><td class="detail">Role play, group discussion</td></tr>
    </table>
  </section>

  <section class="outcomes">
    <h2>Learning Outcomes</h2>
    <p class="outcomes-intro">Training will enable participants to perform their role of Contact Officer and to understand:</p>
    <ol>
      <li>1 The role and responsibilities of a Contact Officer</li>
      <li>2 What amounts to unlawful workplace behaviour</li>
      <li>3 What is considered inappropriate behaviour in our workplace</li>
      <li>4 How to apply understanding unlawful/inappropriate behaviour to common scenarios</li>
      <li>5 How to address and resolve grievances early</li>
      <li>6 Options to resolve grievances internally and the Contact Officer role</li>
      <li>7 External options and their pros and cons for resolving grievances</li>
    </ol>
  </section>

  <div class="brand"><span class="brand-dot"></span>Brindle Legal</div>
  <address class="contact" style="font-style:normal">
    www.brindlelegal.com.au<br>
    18 Harrow Lane, Sandy Bay and Level 4,<br>
    212 Flinders Way, Melbourne.<br>
    Ph: 1300 55 0142 | Email: info@brindlelegal.com.au
  </address>
</article>
</body>
</html>
```